Set up small scale company website

We need a website set up for our educational consultancy - Kelvra Learning. We like the following site and want something similar www.plindaworks.co.uk We can provide the copy and images but need the following:- setting up the overall theme and design - to our requirements on colours and forma- Approximately 4 pages of services offered and with an index pageEtct (yellow and green)And the following pages - as well as a home page:- A contact page linked to our email addresses and registered business address 47 Bramwick Lane, Harwich, Essex, CO14 8RJ- About Us page - An index of services page that links to between 4-6 pages outlining services- A News page that links to updates of latest services, events and activities - easily updated by usOn the homepage we'd like links to Chirpline and Linkboard feeds and links to our other blogs and websites
Target Market(s)
Schools, local authoroties and multi-academy trusts
Logo Text
Kelvra Learning
Coding
Coded - Design and coding required
Number of Pages Required
5+ page
Font styles to use
Requirements
Should not have
- No tacky pictures of mortar boards or chalk boards etc.

```html
<!DOCTYPE html>
<html lang="en">
<head>
<meta charset="utf-8">
<title>Kelvra Learning</title>
<link href="https://fonts.googleapis.com/css2?family=Lato:wght@400;700;900&display=swap" rel="stylesheet">
<style>
:root{
  --green:#8cc63e;
  --green-dark:#6fa62a;
  --yellow:#f4e01a;
  --ink:#222222;
  --dark:#2b2b2b;
  --grey:#8a8a8a;
  --line:#cfcfcf;
  --white:#ffffff;
}
*{margin:0;padding:0;box-sizing:border-box}
html,body{width:1200px;height:4276px;overflow:hidden}
body{font-family:'Lato',sans-serif;color:var(--ink);background:var(--white);position:relative}
.abs{position:absolute}
.site-header{position:absolute;left:0;top:0;width:1200px;height:120px;background:var(--white);border-top:6px solid var(--green);z-index:3}
.brand{position:absolute;left:112px;top:46px;display:flex;align-items:center;gap:14px;font-weight:700;font-size:34px;color:var(--ink)}
.brand-mark{width:38px;height:38px;background:var(--green);border-radius:50%}
.top-address{position:absolute;right:110px;top:22px;font-size:14px;color:#444;display:flex;align-items:center;gap:10px}
.top-address i{width:26px;height:26px;border-radius:50%;background:var(--green);display:block}
.main-nav{position:absolute;right:110px;top:72px;display:flex;gap:42px;font-size:15px;font-weight:700;letter-spacing:.5px;align-items:center}
.main-nav .search{width:16px;height:16px;border:2px solid #333;border-radius:50%;margin-left:20px}
.hero{position:absolute;left:0;top:120px;width:1200px;height:730px;background:linear-gradient(120deg,#d9c3b0 0%,#b89a85 35%,#7e6a5d 70%,#9ea55c 100%)}
.hero-panel{position:absolute;left:0;top:280px;width:480px;height:285px;background:rgba(40,40,40,.55);padding:36px 0 0 42px}
.hero-panel h1{color:var(--yellow);font-size:50px;font-weight:900;line-height:1}
.hero-panel p{color:var(--white);font-size:17px;line-height:28px;margin-top:20px;width:400px}
.btn{display:inline-block;background:var(--green);color:var(--white);font-weight:900;font-size:15px;letter-spacing:.5px;padding:12px 30px;border:2px solid var(--white);box-shadow:0 0 0 2px var(--green)}
.hero-panel .btn{margin-top:26px;padding:10px 28px}
.dots{position:absolute;left:558px;top:740px;display:flex;gap:8px}
.dots i{width:12px;height:12px;border-radius:50%;background:var(--white);display:block}
.dots i.on{background:var(--yellow)}
.wave{position:absolute;left:0;width:1200px;display:block}
.welcome{position:absolute;left:0;top:850px;width:1200px;height:650px;background:linear-gradient(180deg,#f6f6f6,#e8e4e0)}
.welcome-veil{position:absolute;inset:0;background:rgba(255,255,255,.78)}
.ghost{position:absolute;font-weight:900;color:rgba(0,0,0,.06);letter-spacing:4px}
.section-title{position:absolute;left:0;width:1200px;text-align:center;font-weight:900;font-size:44px}
.welcome p{position:absolute;left:210px;top:255px;width:780px;text-align:center;font-size:15px;line-height:40px;color:#777}
.services{position:absolute;left:0;top:1530px;width:1200px;height:640px;background:linear-gradient(180deg,#3a3a3a,#2b2b2b)}
.services .section-title{color:var(--white)}
.hub{position:absolute;left:492px;top:254px;width:216px;height:216px;border-radius:50%;background:var(--white);border:8px solid var(--dark);box-shadow:0 0 0 3px #666}
.hub i{position:absolute;left:58px;top:72px;width:84px;height:56px;background:var(--green);border-radius:6px}
.svc-icon{position:absolute;width:90px;height:90px;border-radius:50%;background:var(--green);border:6px solid #4a4a4a;box-shadow:0 0 0 3px #666}
.svc{position:absolute;width:250px}
.svc h3{color:var(--yellow);font-size:19px;font-weight:900;margin-bottom:10px}
.svc p{color:#ddd;font-size:13.5px;line-height:24px}
.svc.left{text-align:right}
.feeds{position:absolute;left:0;top:2160px;width:1200px;height:655px;background:var(--green)}
.card{position:absolute;top:240px;width:305px;height:300px;background:var(--white);border-top:4px solid var(--ink)}
.card-head{height:58px;border-bottom:1px solid #e3e3e3;display:flex;align-items:center;padding:0 18px;justify-content:space-between}
.card-head h4{font-size:22px;font-weight:900}
.card-head .name{font-size:24px;font-weight:700;color:var(--ink)}
.avatar{width:40px;height:40px;border-radius:50%;background:#c9a993}
.arrows{display:flex;gap:4px}.arrows i{width:20px;height:20px;border-radius:50%;background:var(--green);display:block}
.news-item{display:flex;gap:14px;padding:16px 16px 0}
.news-item .thumb{width:92px;height:90px;background:linear-gradient(135deg,#c69b7e,#5f7fa8)}
.news-item h5{font-size:16px;font-weight:700}
.news-item .date{color:var(--green-dark);font-size:11px;margin:5px 0}
.news-item p{font-size:11px;color:#888;line-height:15px}
.tweet{display:flex;gap:14px;padding:18px 18px 0}
.tweet .bird{width:28px;height:22px;border-radius:50%;background:#2f8ed6;flex:none;margin-top:4px}
.tweet p{font-size:11px;color:#666;line-height:17px}
.tweet .ago{color:var(--green-dark);font-size:10px;margin-top:4px}
.card-foot{position:absolute;bottom:14px;left:18px;right:18px;display:flex;justify-content:space-between;font-size:9px;color:#555}
.post{display:flex;gap:12px;padding:16px 16px 0}
.post .pic{width:56px;height:56px;background:#c7a08a;flex:none}
.post .box{flex:1;border:1px solid #ddd;height:56px;position:relative;font-size:9px;color:#aaa;padding:6px}
.post .share{position:absolute;right:6px;bottom:6px;background:#2d77b3;color:#fff;font-size:9px;font-weight:700;padding:3px 8px}
.contact{position:absolute;left:0;top:2815px;width:1200px;height:900px;background:linear-gradient(180deg,#f4f2ef,#e5ded6)}
.contact-veil{position:absolute;inset:0;background:rgba(255,255,255,.82)}
.field{position:absolute;font-size:15px;color:#333}
.field span{display:block;margin-bottom:16px}
.field i{display:block;height:44px;background:var(--white);border:1px solid #aaa;border-radius:3px}
.site-footer{position:absolute;left:0;top:3790px;width:1200px;height:486px;background:var(--dark);color:var(--white)}
.site-footer h6{position:absolute;top:70px;font-size:17px;font-weight:900;letter-spacing:.3px}
.site-footer h6::after{content:"";display:block;width:34px;height:3px;background:var(--green);margin-top:8px}
.f-row{position:absolute;display:flex;gap:18px;font-size:13px;line-height:26px}
.f-row i{width:50px;height:50px;border-radius:50%;border:2px solid #fff;display:block;flex:none}
.links{position:absolute;left:541px;top:125px;list-style:none;font-size:13px;line-height:27px}
.links li::before{content:"»";margin-right:26px}
.email{position:absolute;left:798px;top:172px;width:260px;height:40px;border:1px solid #666;border-radius:20px;font-size:12px;color:#999;padding:12px 18px}
.signup{position:absolute;left:798px;top:228px;background:var(--yellow);color:var(--ink);font-weight:900;font-size:13px;border-radius:20px;padding:10px 20px}
.rule{position:absolute;top:300px;height:1px;background:#555}
.socials{position:absolute;left:497px;top:255px;display:flex;gap:12px}
.socials i{width:42px;height:42px;border-radius:50%;border:2px solid #fff;display:block}
.copy{position:absolute;left:0;top:425px;width:1200px;text-align:center;font-size:12px;color:#ddd}
</style>
</head>
<body>

<header class="site-header">
  <div class="brand"><span class="brand-mark"></span>Kelvra Learning</div>
  <div class="top-address"><i></i>Ms. Orla Penhallow, 47 Bramwick Lane, Harwich, Essex, CO14 8RJ</div>
  <nav class="main-nav"><span>HOME</span><span>SERVICES</span><span>NEWS</span><span>ABOUT US</span><span>CONTACT US</span><span class="search"></span></nav>
</header>

<section class="hero" role="img" aria-label="Photo of a young girl writing at a classroom desk">
  <div class="hero-panel">
    <h1>KELVRA LEARNING</h1>
    <p>At vero eos etcusamus et iusto odio dignissimos ducimus qui blitis praesentium voluptatum</p>
    <span class="btn">READ MORE</span>
  </div>
  <div class="dots"><i></i><i></i><i class="on"></i><i></i><i></i></div>
</section>
<svg class="wave" style="top:780px;z-index:2" width="1200" height="90" viewBox="0 0 1200 90" preserveAspectRatio="none">
  <path d="M0 40 C300 90 500 0 800 20 C1000 35 1120 40 1200 20 L1200 90 L0 90Z" fill="#f4e01a"/>
  <path d="M0 55 C300 100 500 15 800 35 C1000 48 1120 55 1200 35 L1200 90 L0 90Z" fill="#8cc63e"/>
  <path d="M0 66 C300 110 500 28 800 48 C1000 60 1120 66 1200 48 L1200 90 L0 90Z" fill="#f4f4f4"/>
</svg>

<section class="welcome" role="img" aria-label="Faded photo of smiling pupils in a classroom">
  <div class="welcome-veil"></div>
  <div class="ghost" style="left:1000px;top:60px;font-size:110px;writing-mode:vertical-rl;transform:rotate(180deg)">WELCOME</div>
  <h2 class="section-title" style="top:160px">WELCOME TO KELVRA LEARNING</h2>
  <p>At vero eos et accusamus et iusto odio dignissimos ducimus qui blanditiis praesentium voluptatum deleniti atque corrupti quos dolores et quas molestias excepturi sint occaecati cupiditate non provident, similique sunt in culpa qui officia deserunt mollitia animi id est laborum et dolorum fuga harum quidem rerum facilis est expedita distinctio nam libero tempore cum soluta nobis est eligendi optio cumque nihil impedit quo minus id quod maxime placeat facere possimus omnis voluptas assumenda est omnis dolor repellendus.</p>
  <span class="btn abs" style="left:512px;top:456px">READ MORE INFO</span>
</section>
<svg class="wave" style="top:1460px;z-index:2" width="1200" height="90" viewBox="0 0 1200 90" preserveAspectRatio="none">
  <path d="M0 10 C250 60 450 50 700 40 C950 30 1100 10 1200 30 L1200 90 L0 90Z" fill="#f4e01a"/>
  <path d="M0 28 C250 78 450 68 700 58 C950 48 1100 28 1200 48 L1200 90 L0 90Z" fill="#3a3a3a"/>
</svg>

<section class="services" role="img" aria-label="Darkened photo of pupils working together">
  <div class="ghost" style="left:0;width:1200px;text-align:center;top:85px;font-size:92px;color:rgba(255,255,255,.12)">SERVICES</div>
  <h2 class="section-title" style="top:118px">SERVICES</h2>
  <div class="hub"><i></i></div>
  <div class="svc-icon" style="left:368px;top:269px"></div>
  <div class="svc-icon" style="left:745px;top:269px"></div>
  <div class="svc-icon" style="left:400px;top:417px"></div>
  <div class="svc-icon" style="left:710px;top:417px"></div>
  <div class="svc left" style="left:90px;top:268px"><h3>AT VEROCCU</h3><p>Nam libero temporecum soluta nobis est eligendi optio cumque nihil</p></div>
  <div class="svc" style="left:863px;top:268px"><h3>DIGNISSIMOS</h3><p>Nam libero temporecum soluta nobis est eligendi optio cumque nihil</p></div>
  <div class="svc left" style="left:125px;top:416px"><h3>OLUPTATIB</h3><p>Nam libero temporecum soluta nobis est eligendi optio cumque nihil</p></div>
  <div class="svc" style="left:828px;top:416px"><h3>ATQUERRUPTI</h3><p>Nam libero temporecum soluta nobis est eligendi optio cumque nihil</p></div>
</section>
<svg class="wave" style="top:2135px;z-index:2" width="1200" height="100" viewBox="0 0 1200 100" preserveAspectRatio="none">
  <path d="M0 0 L1200 0 L1200 10 C1000 60 700 30 450 30 C250 30 100 50 0 40Z" fill="#2b2b2b"/>
  <path d="M0 40 C100 50 250 30 450 30 C700 30 1000 60 1200 10 L1200 100 L0 100Z" fill="#f4e01a"/>
  <path d="M0 62 C100 72 250 52 450 52 C700 52 1000 82 1200 32 L1200 100 L0 100Z" fill="#8cc63e"/>
</svg>

<section class="feeds">
  <div class="ghost" style="left:1105px;top:230px;font-size:80px;color:rgba(255,255,255,.18);writing-mode:vertical-rl;transform:rotate(180deg)">NEWS</div>
  <article class="card" style="left:114px">
    <div class="card-head"><h4>LATEST NEWS</h4><div class="arrows"><i></i><i></i></div></div>
    <div class="news-item"><div class="thumb" role="img" aria-label="Photo of pupils at a desk"></div><div><h5>Dignissimos ducimus</h5><div class="date">Admin | Jan 2019</div><p>Ancillae adipisci electram eu cu sit eligendi autem alterum</p></div></div>
    <div class="news-item"><div class="thumb" role="img" aria-label="Photo of pupils reading"></div><div><h5>Dignissimos ducimus</h5><div class="date">Admin | Jan 2019</div><p>Ancillae adipisci electram eu cu sit eligendi autem alterum</p></div></div>
  </article>
  <article class="card" style="left:447px">
    <div class="card-head"><span class="name">Chirpline</span><span class="avatar" role="img" aria-label="Profile photo"></span></div>
    <div class="tweet"><i class="bird"></i><div><p>Ancillae adipisci electram eu cu sit putant verear alterum eu</p><p class="ago">2 hours ago</p></div></div>
    <div class="tweet"><i class="bird"></i><div><p>Ancillae adipisci electram eu cu sit putant verear alterum eu</p><p class="ago">2 hours ago</p></div></div>
    <div class="card-foot"><span>LIKE</span><span>COMMENT</span><span>UNLIKE</span></div>
  </article>
  <article class="card" style="left:781px">
    <div class="card-head"><span class="name">Linkboard</span><span class="avatar" role="img" aria-label="Profile photo"></span></div>
    <div class="post"><span class="pic" role="img" aria-label="Member photo"></span><div class="box">Share an update with us...<br>Attach file<span class="share">SHARE</span></div></div>
    <div class="post"><span class="pic" role="img" aria-label="Member photo"></span><div class="box">Share an update with us...<br>Attach file<span class="share">SHARE</span></div></div>
    <div class="card-foot"><span>LIKE</span><span>COMMENT</span><span>UNLIKE</span></div>
  </article>
</section>

<section class="contact" role="img" aria-label="Faded photo of children in a classroom">
  <div class="contact-veil"></div>
  <h2 class="section-title" style="top:140px">CONTACT US</h2>
  <label class="field" style="left:128px;top:272px;width:450px"><span>Name (First and Last)</span><i></i></label>
  <label class="field" style="left:621px;top:272px;width:448px"><span>Address</span><i></i></label>
  <label class="field" style="left:128px;top:375px;width:450px"><span>Email Address</span><i></i></label>
  <label class="field" style="left:621px;top:375px;width:448px"><span>Phone Number</span><i></i></label>
  <label class="field" style="left:128px;top:480px;width:941px"><span>Message</span><i style="height:130px"></i></label>
  <span class="btn abs" style="left:500px;top:712px">SUBMIT MESSAGE</span>
</section>
<svg class="wave" style="top:3660px;z-index:2" width="1200" height="140" viewBox="0 0 1200 140" preserveAspectRatio="none">
  <path d="M0 10 C200 110 500 110 800 80 C1000 60 1120 40 1200 30 L1200 140 L0 140Z" fill="#f4e01a"/>
  <path d="M0 32 C200 132 500 132 800 102 C1000 82 1120 62 1200 52 L1200 140 L0 140Z" fill="#8cc63e"/>
  <path d="M0 50 C200 150 500 150 800 120 C1000 100 1120 80 1200 70 L1200 140 L0 140Z" fill="#2b2b2b"/>
</svg>

<footer class="site-footer">
  <h6 style="left:143px">CONTACT US</h6>
  <div class="f-row" style="left:143px;top:126px"><i></i><span>Ms. Orla Penhallow, 47 Bramwick Lane,<br>Harwich, Essex, CO14 8RJ</span></div>
  <div class="f-row" style="left:143px;top:200px"><i></i><span>Phone :<br>01255 604 719</span></div>
  <h6 style="left:541px">QUICK LINKS</h6>
  <ul class="links"><li>Home</li><li>Services</li><li>News</li><li>About us</li><li>Contact us</li></ul>
  <h6 style="left:798px">SIGN UP NEWSLETTER</h6>
  <p class="abs" style="left:798px;top:130px;font-size:12px">Atro eos et accusamus et iusimos ducimus</p>
  <div class="email">Enter Email</div>
  <span class="signup">SIGN UP</span>
  <div class="rule" style="left:100px;width:385px"></div>
  <div class="rule" style="left:715px;width:385px"></div>
  <div class="socials"><i></i><i></i><i></i><i></i></div>
  <p class="copy">© copyright 2019 Kelvra Learning. All Rights Reserved &nbsp;|&nbsp; Privacy policy</p>
</footer>

</body>
</html>
```